BOLD & MINIMALIST DESIGN NEEDED

We want a very bold but minimalistic business card design that is impactful and utilizes both sides of the business card. Our current logo is included for your use.

We want bold fonts and good use of negative space. We don't want the logo to overpower the design.

Target Market(s)

Professionals who are building new commercial buildings.

Industry/Entity Type

Construction

Contact Information for Business Card

Name, Title, email, office phone, cell phone, website

Font styles to use
Serif
Sans Serif

Requirements
Must have
• Bold design!

```html
<!DOCTYPE html>
<html lang="en">
<head>
<meta charset="utf-8">
<title>Stonecrest Design + Build — Business Card</title>
<link rel="stylesheet" href="https://fonts.googleapis.com/css2?family=Raleway:ital,wght@0,400;0,500;0,800;1,400&display=swap">
<style>
  :root {
    --backdrop: #808080;
    --card: #ffffff;
    --ink: #141414;
    --green: #7dc242;
  }
  * { box-sizing: border-box; margin: 0; padding: 0; }
  html, body {
    width: 1200px;
    height: 800px;
    overflow: hidden;
    background: var(--backdrop);
    font-family: "Raleway", sans-serif;
    color: var(--ink);
  }
  .canvas {
    position: relative;
    width: 1200px;
    height: 800px;
  }
  .card {
    position: absolute;
    width: 620px;
    height: 354px;
    background: var(--card);
  }
  .card--front { left: 40px; top: 40px; }
  .card--back  { left: 540px; top: 406px; }

  /* Front side */
  .brand-mark {
    position: absolute;
    display: flex;
    align-items: center;
    gap: 8px;
  }
  .brand-mark__square {
    width: 14px;
    height: 14px;
    background: var(--green);
    flex: none;
  }
  .brand-mark__name {
    font-weight: 800;
    color: var(--ink);
    letter-spacing: 0.02em;
    text-transform: uppercase;
    line-height: 1;
  }
  .card--front .brand-mark {
    right: 40px;
    top: 78px;
  }
  .card--front .brand-mark__name { font-size: 22px; }

  .contact {
    position: absolute;
    left: 37px;
    top: 196px;
    list-style: none;
  }
  .contact__name {
    font-size: 19px;
    font-weight: 500;
    margin-bottom: 8px;
  }
  .contact__title {
    font-size: 15px;
    font-style: italic;
    color: var(--green);
    margin-bottom: 7px;
  }
  .contact__line {
    font-size: 14px;
    margin-bottom: 6px;
    font-variant-numeric: oldstyle-nums;
  }
  .contact__line--office { color: var(--green); }
  .contact__line--cell { font-style: italic; }

  /* Back side */
  .card--back .brand-mark {
    left: 50%;
    top: 150px;
    transform: translateX(-50%);
    gap: 12px;
  }
  .card--back .brand-mark__square { width: 22px; height: 22px; }
  .card--back .brand-mark__name { font-size: 30px; white-space: nowrap; }
  .website {
    position: absolute;
    left: 0;
    right: 0;
    top: 284px;
    text-align: center;
    font-size: 14px;
    font-weight: 800;
  }
</style>
</head>
<body>
<main class="canvas">
  <section class="card card--front" aria-label="Card front">
    <div class="brand-mark">
      <span class="brand-mark__square"></span>
      <span class="brand-mark__name">Stonecrest</span>
    </div>
    <ul class="contact">
      <li class="contact__name">Jonah Whitfield</li>
      <li class="contact__title">Founder &amp; Owner</li>
      <li class="contact__line">hello@stonecrest-build.com</li>
      <li class="contact__line contact__line--office">555-310-4820</li>
      <li class="contact__line contact__line--cell">555-310-7734</li>
    </ul>
  </section>

  <section class="card card--back" aria-label="Card back">
    <div class="brand-mark">
      <span class="brand-mark__square"></span>
      <span class="brand-mark__name">Stonecrest Design + Build</span>
    </div>
    <p class="website">stonecrest-build.com</p>
  </section>
</main>
</body>
</html>
```